Business Card Design Project

I need some business cards with the logo you did for us (attached)
I am looking for a coulourful yet serious business card

We do market research
on the back I want the logo

on the front my name : Corinne Valdessac
position : Manager
address : Brume Analytica Sarl - 27 Rue des tanneurs
1847 Glarency - Switzerland
corinne.valdessac@brumeanalytica.ch
Tel : +4122 934 07 58
Mob France :+33 671 42 8356
Mob Italy +39 347 520 8163

The tree of the logo could also be used alone

THE BACKGROUND COLOR ON THE FRONT HAS TO BE WHITE, ON THE BACK YU CAN TRY OHER COLOUR BUT HOMOGENEOUS (NOT EXPENSIVE TO PRINT)

Target Market(s)

multinational companies or other market research companies

Industry/Entity Type

Market Research

Requirements
Must have
• logo on the back
and all the info above

```html
<!DOCTYPE html>
<html lang="en">
<head>
<meta charset="utf-8">
<title>Brume Analytica – Business Cards</title>
<link rel="stylesheet" href="https://fonts.googleapis.com/css2?family=Arimo:wght@400;700&display=swap">
<style>
  :root {
    --stage: #3b3b3d;
    --raspberry: #d42560;
    --raspberry-dark: #c8214f;
    --crimson-band: #b01f2e;
    --paper: #f2f2f2;
    --cocoa: #6b3a2e;
    --ink: #3a2a26;
    --grey: #555555;
    --white: #ffffff;
  }
  * { margin: 0; padding: 0; box-sizing: border-box; }
  html, body {
    width: 1200px; height: 534px; overflow: hidden;
    background: var(--stage);
    font-family: "Arimo", Arial, sans-serif;
  }
  .stage { position: relative; width: 1200px; height: 534px; }

  .card {
    position: absolute; top: 118px; height: 298px;
    border-radius: 22px; overflow: hidden;
  }
  .card--back { left: 62px; width: 506px; background: var(--raspberry); }
  .card--front { left: 622px; width: 524px; background: var(--paper); }

  /* wordmark */
  .wordmark { position: absolute; display: flex; align-items: center; gap: 10px; }
  .wordmark__dot { border-radius: 50%; flex: none; }
  .wordmark__name { font-weight: 400; white-space: nowrap; line-height: 1; }

  .card--back .wordmark { left: 20px; top: 214px; }
  .card--back .wordmark__dot { width: 26px; height: 26px; background: var(--cocoa); }
  .card--back .wordmark__name { font-size: 42px; color: var(--cocoa); letter-spacing: -0.5px; }
  .card--back .web {
    position: absolute; left: 134px; top: 264px;
    font-size: 12px; line-height: 14px; letter-spacing: 1.6px; color: var(--white);
  }

  .card--front .wordmark { left: 14px; top: 168px; }
  .card--front .wordmark__dot { width: 20px; height: 20px; background: var(--raspberry-dark); }
  .card--front .wordmark__name { font-size: 30px; color: var(--raspberry-dark); letter-spacing: -0.4px; }

  .holder { position: absolute; left: 213px; top: 74px; white-space: nowrap; }
  .holder__name { font-size: 17px; font-weight: 700; color: var(--raspberry-dark); }
  .holder__role { font-size: 12px; color: var(--grey); margin-left: 4px; }

  .address {
    position: absolute; left: 213px; top: 100px; width: 311px; height: 32px;
    background: var(--crimson-band); color: var(--white);
    font-size: 12px; line-height: 14px; padding: 2px 0 0 10px;
  }

  .contacts { position: absolute; left: 266px; top: 146px; list-style: none; }
  .contacts li { font-size: 12px; line-height: 16px; color: var(--ink); white-space: nowrap; }
  .contacts .label { font-size: 10px; color: var(--raspberry-dark); }

  .web-band {
    position: absolute; left: 0; top: 220px; width: 100%; height: 44px;
    background: var(--raspberry); color: var(--white);
    font-size: 18px; letter-spacing: 2.6px; text-align: center; line-height: 44px;
  }
</style>
</head>
<body>
<main class="stage">

  <section class="card card--back" aria-label="Card back">
    <div class="wordmark">
      <span class="wordmark__dot"></span>
      <span class="wordmark__name">brume analytica</span>
    </div>
    <p class="web">www.brumeanalytica.ch</p>
  </section>

  <section class="card card--front" aria-label="Card front">
    <div class="wordmark">
      <span class="wordmark__dot"></span>
      <span class="wordmark__name">brume analytica</span>
    </div>

    <p class="holder">
      <span class="holder__name">Corinne Valdessac</span>
      <span class="holder__role">Manager</span>
    </p>

    <p class="address">Brume Analytica Sarl - 27 Rue des tanneurs<br>1847 Glarency - Switzerland</p>

    <ul class="contacts">
      <li><span class="label">tel :</span> +4122 934 07 58</li>
      <li><span class="label">mob france :</span> +33 671 42 8356</li>
      <li><span class="label">mob italy :</span> +39 347 520 8163</li>
      <li><span class="label">email :</span> corinne.valdessac@brumeanalytica.ch</li>
    </ul>

    <p class="web-band">www.brumeanalytica.ch</p>
  </section>

</main>
</body>
</html>
```